E-book named 'Harbourlight: A Field Manual for Purpose Builders' needs cover

I need a cover for my ebook and also paper back book.
I need a very appealing cover for my ebook. Social enterprise is a company that gives something back to the society as opposed to only make profit.
The society and its people always benefit.
So far the above is the name chosen but I welcome small changes and ideas also a tag line would also be great something like “everything you need to know to sep up a social enterprise and succeed”
I want to write in the cover something to make people buy it. I want the name Social Enterprise in more evidence ...
Target Market(s)
Students, graduates and business minded people who are thinking of set up a social enterprise company and needs guidance
Industry/Entity Type
It Company
Colors
Designer to choose colors to be used in the design.
Look and feel
Each slider illustrates characteristics of the customer's brand and the style your logo design should communicate.

```html
<!DOCTYPE html>
<html lang="en">
<head>
<meta charset="utf-8">
<title>Harbourlight: A Field Manual for Purpose Builders — Cover</title>
<link rel="stylesheet" href="https://fonts.googleapis.com/css2?family=Jost:wght@300;400;500;700&display=swap">
<style>
  :root {
    --page-bg: #ecebe8;
    --cover-ink: #0c1016;
    --cover-glow: #3a4a5e;
    --accent-blue: #1e9ce0;
    --accent-orange: #f39a10;
    --title-light: #dde5ee;
  }
  * { margin: 0; padding: 0; box-sizing: border-box; }
  html, body {
    width: 1200px;
    height: 800px;
    overflow: hidden;
    background: var(--page-bg);
  }
  .stage {
    width: 1200px;
    height: 800px;
    display: flex;
    align-items: center;
    justify-content: center;
  }
  .cover {
    position: relative;
    width: 480px;
    height: 740px;
    background: var(--cover-ink);
    overflow: hidden;
    text-align: center;
    font-family: "Jost", "Futura", sans-serif;
  }
  .cover__hands {
    position: absolute;
    left: 0;
    top: 300px;
    width: 480px;
    height: 360px;
    background:
      radial-gradient(ellipse 46% 42% at 55% 45%, #6f8092 0%, #3c4a5a 38%, #18202a 70%, var(--cover-ink) 100%);
  }
  .cover__publisher {
    position: absolute;
    top: 34px;
    left: 0;
    right: 0;
    color: var(--accent-blue);
    font-weight: 300;
    font-size: 21px;
    letter-spacing: 4px;
  }
  .cover__title {
    position: absolute;
    top: 104px;
    left: 0;
    right: 0;
  }
  .cover__title-lead {
    display: block;
    color: var(--title-light);
    font-weight: 300;
    font-size: 33px;
    line-height: 42px;
    letter-spacing: 3px;
  }
  .cover__title-main {
    display: block;
    margin-top: 8px;
    color: var(--accent-orange);
    font-weight: 700;
    font-size: 66px;
    line-height: 68px;
    letter-spacing: 5px;
  }
  .cover__tagline {
    position: absolute;
    bottom: 34px;
    left: 0;
    right: 0;
    color: var(--accent-blue);
    font-weight: 500;
    font-size: 19px;
    line-height: 26px;
    letter-spacing: 1.2px;
  }
</style>
</head>
<body>
  <main class="stage">
    <section class="cover">
      <div class="cover__hands" role="img" aria-label="Dark blue-toned photograph of clasped hands held together in support"></div>
      <p class="cover__publisher">TIDEWATER &amp; FERN</p>
      <h1 class="cover__title">
        <span class="cover__title-lead">HARBOURLIGHT:</span>
        <span class="cover__title-lead">A FIELD MANUAL FOR</span>
        <span class="cover__title-main">PURPOSE<br>BUILDERS</span>
      </h1>
      <p class="cover__tagline">EVERYTHING YOU NEED TO KNOW<br>TO SEP UP A SOCIAL ENTERPRISE<br>AND SUCCEED</p>
    </section>
  </main>
</body>
</html>
```